Business IT Services Billboard to attract local small businesses

We are Brivolane, a premier Managed Service Provider (MSP) specializing in comprehensive IT services and VOIP phone solutions exclusively for businesses. Our goal is to create a dynamic and visually engaging billboard advertisement that not only highlights our cutting-edge IT solutions but also emphasizes our state-of-the-art VOIP phone services. This billboard should communicate our commitment to providing innovative, reliable, and holistic technology solutions.
Target Market(s)
small business
Industry/Entity Type
Information Technology
Colors
Designer to choose colors to be used in the design.
Look and feel
Each slider illustrates characteristics of the customer's brand and the style your logo design should communicate.

```html
<!DOCTYPE html>
<html lang="en">
<head>
<meta charset="utf-8">
<title>Brivolane Billboard</title>
<link href="https://fonts.googleapis.com/css2?family=Montserrat:wght@400;500;700;800&display=swap" rel="stylesheet">
<style>
  :root {
    --page-bg: #eef1f5;
    --brand-blue: #0b66b0;
    --panel-dark: #0a4f8c;
    --panel-light: #1665a8;
    --navy: #1b3a6b;
    --white: #ffffff;
    --chip-grey: #d9dadc;
    --photo-a: #8a8f96;
    --photo-b: #c9a26a;
    --photo-c: #9fb8d6;
  }
  html, body {
    margin: 0;
    width: 1189px;
    height: 1200px;
    overflow: hidden;
    background: var(--page-bg);
    font-family: "Montserrat", Arial, sans-serif;
  }
  .billboard {
    position: absolute;
    left: 44px;
    top: 440px;
    width: 1100px;
    height: 319px;
    overflow: hidden;
    background: var(--white);
  }
  .billboard-shapes {
    position: absolute;
    inset: 0;
  }
  .brand-name {
    position: absolute;
    left: 36px;
    top: 12px;
    margin: 0;
    font-size: 62px;
    font-weight: 800;
    letter-spacing: 3px;
    line-height: 66px;
    color: var(--brand-blue);
  }
  .headline {
    position: absolute;
    left: 36px;
    top: 94px;
    margin: 0;
    font-size: 35px;
    font-weight: 800;
    line-height: 39px;
    color: var(--white);
  }
  .subline {
    position: absolute;
    left: 36px;
    top: 218px;
    margin: 0;
    padding-left: 8px;
    border-left: 2px solid var(--white);
    font-size: 15px;
    font-weight: 500;
    line-height: 17px;
    color: var(--white);
  }
  .web-cta {
    position: absolute;
    left: 42px;
    top: 272px;
    color: var(--panel-dark);
  }
  .web-cta-label {
    display: block;
    font-size: 9.5px;
    font-weight: 500;
    color: var(--navy);
    line-height: 11px;
  }
  .web-cta-url {
    display: block;
    font-size: 21px;
    font-weight: 700;
    line-height: 24px;
  }
  .phone-number {
    position: absolute;
    left: 410px;
    top: 276px;
    font-size: 25px;
    font-weight: 700;
    line-height: 30px;
    color: var(--navy);
  }
</style>
</head>
<body>
  <section class="billboard">
    <svg class="billboard-shapes" width="1100" height="319" viewBox="0 0 1100 319" aria-hidden="false">
      <defs>
        <radialGradient id="panelGradient" cx="0.55" cy="0.45" r="0.7">
          <stop offset="0" stop-color="var(--panel-light)"/>
          <stop offset="1" stop-color="var(--panel-dark)"/>
        </radialGradient>
        <linearGradient id="photoGradient" x1="0" y1="0" x2="1" y2="1">
          <stop offset="0" stop-color="var(--photo-a)"/>
          <stop offset="0.5" stop-color="var(--photo-b)"/>
          <stop offset="1" stop-color="var(--photo-c)"/>
        </linearGradient>
      </defs>
      <polygon class="blue-panel" points="0,0 688,0 581,319 0,319" fill="url(#panelGradient)"/>
      <polygon class="logo-band" points="0,0 690,0 662,78 0,78" fill="var(--white)"/>
      <polygon class="accent-stripe" points="700,0 710,0 624,258 614,258" fill="var(--panel-dark)"/>
      <polygon class="team-photo" points="716,0 1100,0 1100,319 672,319" fill="url(#photoGradient)" role="img" aria-label="Photo of three colleagues in an office gathered around a laptop"/>
      <polygon class="web-chip" points="34,269 368,269 352,313 34,313" fill="var(--white)"/>
      <polygon class="phone-chip" points="376,269 636,269 620,313 360,313" fill="var(--chip-grey)"/>
      <g class="phone-icon" transform="translate(391,291)">
        <circle r="13" fill="none" stroke="var(--panel-dark)" stroke-width="2"/>
        <path d="M-6,-5 l3,-2 l3,4 l-2,2 q1,3 4,4 l2,-2 l4,3 l-2,3 q-9,0 -12,-12z" fill="var(--panel-dark)"/>
        <path d="M2,-7 q5,1 6,6 M2,-4 q2,1 3,3" fill="none" stroke="var(--panel-dark)" stroke-width="1.5"/>
      </g>
    </svg>

    <h1 class="brand-name">BRIVOLANE</h1>
    <h2 class="headline">ELEVATE YOUR BUSINESS<br>WITH NEXT-GEN IT AND<br>VOIP SERVICES</h2>
    <p class="subline">Innovative IT and VOIP Solutions Tailored<br>for Your Business Success.</p>
    <div class="web-cta">
      <span class="web-cta-label">Transform Your Tech Today at</span>
      <span class="web-cta-url">www.brivolane.com</span>
    </div>
    <div class="phone-number">(555) 310-4827</div>
  </section>
</body>
</html>
```